Lantern Holdings Business Card

We are looking to design new business cards for our company. We have two office locations and would like to have both full addresses on the card. Each address needs two lines for the building name and street address and a line or two for the city, state and zip code. There should be a place for 2-3 phone numbers. The addresses and phone numbers are at the bottom of this description. We also need a place to put our company website and one email address. Our logo is attached.
We would like the card to be two sided. The back of the card should have a blue background with some part of our logo design on it. We would like the full logo on the front of the card as well. The front of the card should have a white background with the blue logo. We are open to listing our addresses on the front or the back of the card. The person who designed our logo gave us an excellent business card idea that we really liked. I have attached a picture of his business card idea so that we can build off of it.
Addresses:
The Marlow Exchange
2214 47th Street NW
Washington, DC 20419
Osprey Harbor Tower
815 Tamsin Boulevard #2207
Miami, FL 33987
Phone Numbers: (202) 555-0148
(202) 555-0193
Website: www.lanternholdings-example.com

```html
<!DOCTYPE html>
<html lang="en">
<head>
<meta charset="utf-8">
<title>Lantern Holdings Business Card</title>
<link rel="stylesheet" href="https://fonts.googleapis.com/css2?family=Mulish:wght@400;500;600&display=swap">
<style>
  :root {
    --backdrop: #e4e5e8;
    --card-white: #ffffff;
    --brand-blue: #1f3192;
    --card-blue: #1d3590;
    --panel-blue: #2548b2;
    --text-light: #f3f5fb;
    --rule-light: rgba(255,255,255,0.75);
  }
  * { box-sizing: border-box; margin: 0; padding: 0; }
  html, body {
    width: 1200px; height: 1000px; overflow: hidden;
    background: var(--backdrop);
    font-family: "Mulish", Arial, sans-serif;
  }
  .card {
    position: absolute;
    left: 310px;
    width: 580px;
    height: 340px;
    border-radius: 4px;
    overflow: hidden;
    box-shadow: 0 6px 18px rgba(0,0,0,0.18);
  }
  .card-front {
    top: 70px;
    background: var(--card-white);
  }
  .brand {
    position: absolute;
    left: 0; right: 0; top: 112px;
    display: flex; align-items: center; justify-content: center; gap: 16px;
  }
  .brand-mark {
    width: 62px; height: 62px;
    border-radius: 8px;
    background: var(--brand-blue);
  }
  .brand-name {
    color: var(--brand-blue);
    font-weight: 500;
    font-size: 44px;
    letter-spacing: 1px;
    text-transform: uppercase;
  }
  .website {
    position: absolute;
    left: 0; right: 0; bottom: 50px;
    text-align: center;
    color: var(--brand-blue);
    font-size: 15px;
    letter-spacing: 0.3px;
  }
  .card-back {
    top: 500px;
    background: var(--card-blue);
  }
  .back-panel {
    position: absolute;
    left: 370px; top: 70px;
    width: 260px; height: 300px;
    border-radius: 26px;
    background: var(--panel-blue);
  }
  .contact {
    position: absolute;
    right: 240px; top: 72px;
    color: var(--text-light);
    text-align: right;
    font-size: 15.5px;
    line-height: 1.22;
  }
  .office { padding: 6px 0; }
  .office-name { font-weight: 600; }
  .divider {
    border: 0;
    border-top: 1.5px dotted var(--rule-light);
    margin: 3px 0 3px 0;
  }
  .phones { padding-top: 6px; }
</style>
</head>
<body>
  <section class="card card-front">
    <div class="brand">
      <div class="brand-mark"></div>
      <div class="brand-name">Lantern Holdings</div>
    </div>
    <div class="website">www.lanternholdings-example.com</div>
  </section>

  <section class="card card-back">
    <div class="back-panel"></div>
    <div class="contact">
      <div class="office">
        <div class="office-name">The Marlow Exchange</div>
        <div>2214 47th Street NW</div>
        <div>Washington, DC 20419</div>
      </div>
      <hr class="divider">
      <div class="office">
        <div>Osprey Harbor Tower</div>
        <div>815 Tamsin Boulevard #2207</div>
        <div>Miami, FL 33987</div>
      </div>
      <hr class="divider">
      <div class="phones">
        <div>Ph: (202) 555-0148 | (202) 555-0193</div>
        <div>info@lanternholdings-example.com</div>
      </div>
    </div>
  </section>
</body>
</html>
```